GRAY HARBOR PLAN

Our business will reach out to business owners and offer a variety of services, predominantly the following: a) a free review of the owner's business structure to make sure it was properly formed, b) litigation representation at an extremely discounted rate (we plan to engage in direct marketing to civil litigation defendants, c) weekly "attorney letters" at no charge, d) free legal forms that are commonly used in business, and e) by far, the most important service offered is the licensed use of a copyrighted clause that is incorporated into virtually any commercial agreement (hereafter referred to as "the Clause").
The effect of the Clause is to require that parties to a contract ("Contract") notify each other, in writing, of any fact or event (referred to as "Event") that might impact the Contract. And the failure to comply with the Clause results in the non-complying party being given a significant advantage should the Contract become the subject of a lawsuit, in particular, an advantage over issues commonly referred to "he said / she said" issues. We believe that most civil litigation hinges on at least one or more of such issues, i.e., issues for which there is no concrete proof one way or the other. In such cases, the party taking advantage of the Clause will very likely prevail on all such issues -- in other words, using the Clause will likely prevent litigation from being pursued against such party, or likely result in such party prevailing in court. ARE ALL THESE SERVICES WORTH $9.95 PER WEEK?

Target Market(s)

#1. Current defendants in civil litigation cases, #2 business owners who get sued by: a) employees, b) business associates, who believe they have claims against the owner or the business.

Industry/Entity Type

Legal claims are increasing in large part because of the leverage that exists in forcing businesses to hire legal counsel to defend "he said / she said" claims -

Number of Pages Required

1 page

Colors
0094D4
00A9DD
6FCCEA
C7EBF8
E9F6FB

Requirements
Must have
• Professional appearance. We are explaining that there are wolves out there in the form of employees and business associates who can turn into enemies by making groundless allegations that could easily cost tens of thousands of dollars -- and it does more frequently than you might think.
Nice to have
• I like to refer to Tom Wexley's classic axiom: an ounce of prevention is worth a pound of cure -- with anecdotes taken from actual examples of why the services offered, i.e., the extreme discount of legal fees in the event of a lawsuit, being able to send attorney letters sent out every week at no charge, and above all, the right to incorporate copyrighted contractual provisions that make it very difficult for employees and business associates to make claims against you that evolve into lawsuits -- are each worth far more than the paltry membership fee of $9.95 per week.

```html
<!DOCTYPE html>
<html lang="en">
<head>
<meta charset="utf-8">
<title>Gray Harbor Plan</title>
<link rel="stylesheet" href="https://fonts.googleapis.com/css2?family=Playfair+Display:wght@700;900&family=Roboto:wght@400;500;700&display=swap">
<style>
:root{
  --blue:#0094D4;
  --cyan:#00A9DD;
  --sky:#6FCCEA;
  --ice:#C7EBF8;
  --mist:#E9F6FB;
  --navy:#0d3b56;
  --dark:#14263a;
  --footer:#102031;
  --text:#2b3340;
  --white:#fff;
}
*{box-sizing:border-box;margin:0;padding:0}
html,body{width:1200px;height:4118px;overflow:hidden}
body{position:relative;font-family:"Roboto",sans-serif;color:var(--text);background:var(--white)}
.abs{position:absolute}
.serif{font-family:"Playfair Display",serif;font-weight:700}
.photo{position:absolute}

/* hero */
.hero{left:0;top:0;width:1200px;height:800px;background:linear-gradient(135deg,#1d2c3a 0%,#3a4a58 35%,#5d6c78 55%,#16222e 100%)}
.topbar{left:0;top:0;width:1200px;height:88px;background:rgba(0,0,0,.45)}
.brand{left:45px;top:28px;color:var(--sky);font-size:26px}
.nav{top:28px;left:498px;display:flex;gap:30px;color:var(--white);font-size:22px;letter-spacing:.5px}
.call{top:20px;color:var(--white);font-size:22px;line-height:26px;text-align:center;letter-spacing:1px}
.call-icon{left:942px;top:30px}
.hero-box{left:48px;top:248px;width:839px;height:363px;border:6px solid var(--white)}
.hero-title{left:68px;top:290px;color:var(--sky);font-size:72px;line-height:68px}
.hero-sub{left:68px;top:467px;width:760px;color:var(--white);font-size:21px;line-height:26px}
.btn{position:absolute;display:flex;align-items:center;justify-content:center;font-size:15px;font-weight:700}
.btn-blue{left:141px;top:575px;width:259px;height:68px;background:var(--blue);color:var(--white)}
.btn-light{left:446px;top:575px;width:259px;height:68px;background:var(--sky);color:var(--navy)}
.hero-dots{left:478px;top:740px}

/* intro */
.intro-frame{left:48px;top:855px;width:447px;height:539px;border:4px solid var(--blue)}
.intro-photo{left:70px;top:877px;width:449px;height:542px;background:linear-gradient(160deg,#2e3d4c,#6f8290 55%,#b9c7d0)}
.intro-title{left:579px;top:850px;width:560px;color:var(--blue);font-size:40px;line-height:52px;letter-spacing:1px}
.intro-lead{left:576px;top:970px;width:520px;font-size:20px;line-height:25px;font-weight:700;color:#111}
.features{left:576px;top:1098px;width:560px;list-style:none}
.features li{position:relative;padding-left:47px;font-size:18px;line-height:23px;color:#222}
.features li::before{content:"";position:absolute;left:0;top:12px;width:18px;height:18px;border:3px solid var(--cyan);border-radius:50%}

/* services */
.services{left:0;top:1447px;width:1200px;height:612px;background:var(--mist)}
.services-title{left:0;top:1482px;width:1200px;text-align:center;color:var(--blue);font-size:40px}
.card{position:absolute;top:1565px;width:258px;height:352px}
.card-label{position:absolute;left:20px;top:270px;color:var(--white);font-size:20px;line-height:24px}
.card-label b{display:block;color:var(--sky);font-family:"Playfair Display",serif;font-size:24px}
.card-arrow{position:absolute;left:200px;top:285px}
.btn-outline{left:471px;top:1958px;width:258px;height:61px;border:3px solid var(--blue);color:#222;font-weight:400;font-size:21px}

/* about */
.about-band{left:684px;top:2059px;width:516px;height:647px;background:var(--blue)}
.about-title{left:48px;top:2098px;font-size:38px;color:var(--navy);letter-spacing:1px}
.about-text{left:45px;top:2175px;width:505px;font-size:21.5px;line-height:28px;color:#444}
.about-frame{left:567px;top:2158px;width:150px;height:496px;border:4px solid var(--blue);border-right:none}
.about-photo{left:591px;top:2134px;width:536px;height:499px;background:linear-gradient(150deg,#34414d,#5e6b76 45%,#9fb1bd 80%,#d3dde3)}
.btn-learn{left:48px;top:2564px;width:163px;height:40px;border:3px solid var(--blue);background:var(--white);color:#333;font-weight:400;font-size:20px}

/* testimonials */
.reviews{left:0;top:2706px;width:1200px;height:352px;background:var(--dark)}
.reviews-title{left:0;top:2740px;width:1200px;text-align:center;color:var(--sky);font-size:38px}
.reviews-rule{left:417px;top:2795px;width:366px;height:3px;background:var(--sky)}
.quote{left:150px;top:2900px;width:900px;text-align:center;color:var(--white);font-size:20.5px;line-height:26px}

/* consult + why */
.consult{left:0;top:3058px;width:600px;height:644px;background:var(--blue)}
.why{left:600px;top:3058px;width:600px;height:644px;background:var(--white)}
.block-title{top:3094px;font-size:38px}
.block-text{top:3160px;width:520px;font-size:20px;line-height:25px}
.field{position:absolute;border:2px solid var(--white);color:var(--white);font-size:19px;padding:14px 18px}
.btn-send{left:45px;top:3582px;width:259px;height:63px;border:3px solid var(--white);color:var(--white);font-weight:400;font-size:21px}
.acc{position:absolute;left:646px;width:527px;border:1px solid #8aa3b3}
.acc-head{height:64px;background:var(--ice);display:flex;align-items:center;justify-content:space-between;padding:0 20px;font-size:20px;color:#222}
.acc-body{padding:14px 20px;font-size:14.5px;line-height:18px;color:#333;background:var(--white)}

/* footer */
.footer{left:0;top:3702px;width:1200px;height:416px;background:var(--footer)}
.foot-title{top:3755px;color:var(--sky);font-size:38px}
.foot-line{color:var(--white);font-size:28px;line-height:36px}
.btn-contact{left:48px;top:3925px;width:256px;height:60px;border:3px solid var(--white);color:var(--white);font-weight:400;font-size:20px}
.foot-rule{left:0;top:4068px;width:1200px;height:1px;background:var(--cyan)}
.copyright{left:0;top:4080px;width:1200px;text-align:center;color:var(--white);font-size:20px}
</style>
</head>
<body>

<!-- hero -->
<div class="abs hero" role="img" aria-label="Lawyer seated at a desk in an office with bookshelves"></div>
<div class="abs topbar"></div>
<div class="abs brand serif">GRAY HARBOR</div>
<nav class="abs nav"><span>Home</span><span>Services</span><span>About</span><span>Contact</span></nav>
<svg class="abs call-icon" width="28" height="32" viewBox="0 0 24 24"><path fill="#fff" d="M6.6 10.8a15.1 15.1 0 0 0 6.6 6.6l2.2-2.2c.3-.3.7-.4 1-.2 1.1.4 2.3.6 3.6.6.6 0 1 .4 1 1V20c0 .6-.4 1-1 1C10.6 21 3 13.4 3 4c0-.6.4-1 1-1h3.5c.6 0 1 .4 1 1 0 1.3.2 2.5.6 3.6.1.3 0 .7-.2 1z"/></svg>
<div class="abs call" style="left:975px">Get Us Call<br>+1 555 010 2040</div>
<div class="abs hero-box"></div>
<h1 class="abs hero-title serif">Welcome To<br>GRAY HARBOR PLAN</h1>
<p class="abs hero-sub">Groundless claims from employees and business associates can cost<br>tens of thousands. Protect your business for just $9.95 per week.</p>
<a class="btn btn-blue">GET FREE CONSULTATION</a>
<a class="btn btn-light">READ OUR REVIEWS</a>
<svg class="abs hero-dots" width="244" height="32" viewBox="0 0 244 32">
  <circle cx="16" cy="16" r="14" fill="#00A9DD"/><path d="M24 16H9m6-6-6 6 6 6" stroke="#fff" stroke-width="3" fill="none"/>
  <circle cx="59" cy="16" r="11" fill="#fff"/><circle cx="101" cy="16" r="11" fill="#fff"/>
  <circle cx="143" cy="16" r="11" fill="#00A9DD"/><circle cx="185" cy="16" r="11" fill="#fff"/>
  <circle cx="228" cy="16" r="14" fill="#00A9DD"/><path d="M220 16h15m-6-6 6 6-6 6" stroke="#fff" stroke-width="3" fill="none"/>
</svg>

<!-- intro -->
<div class="abs intro-frame"></div>
<div class="photo intro-photo" role="img" aria-label="Three colleagues reviewing work at a computer"></div>
<h2 class="abs intro-title serif">Highly Skilled Lawyers &amp;<br>Attorneys for you</h2>
<p class="abs intro-lead">One weekly membership covers every service below. The most important is the licensed use of the Clause in your commercial agreements.</p>
<ul class="abs features">
  <li style="margin-bottom:7px">A free review of the owner's business structure to make<br>sure it was properly formed</li>
  <li style="margin-bottom:27px">Litigation representation at an extremely discounted rate</li>
  <li style="margin-bottom:28px">Weekly "attorney letters" at no charge</li>
  <li style="margin-bottom:17px">Free legal forms that are commonly used in business</li>
  <li>The licensed use of a copyrighted clause that is<br>incorporated into virtually any commercial agreement</li>
</ul>

<!-- services -->
<div class="abs services"></div>
<h2 class="abs services-title serif">Services We Provide</h2>
<div class="card" style="left:48px;background:linear-gradient(170deg,#b9c4cc,#4f5d69 55%,#25303a)" role="img" aria-label="Stressed man holding his head">
  <div class="card-label">Business<b>Review</b></div>
  <svg class="card-arrow" width="36" height="26" viewBox="0 0 36 26"><path d="M2 13h30M21 3l11 10-11 10" stroke="#6FCCEA" stroke-width="4" fill="none"/></svg>
</div>
<div class="card" style="left:329px;background:linear-gradient(170deg,#4e6272,#8ea3b2 55%,#d2dde4)" role="img" aria-label="Two colleagues reviewing charts at a table">
  <div class="card-label">Litigation<b>Defense</b></div>
  <svg class="card-arrow" width="36" height="26" viewBox="0 0 36 26"><path d="M2 13h30M21 3l11 10-11 10" stroke="#6FCCEA" stroke-width="4" fill="none"/></svg>
</div>
<div class="card" style="left:612px;background:linear-gradient(170deg,#5b6b78,#8798a5 50%,#24344a)" role="img" aria-label="Worried woman resting her head on her hand">
  <div class="card-label">Attorney<b>Letters</b></div>
  <svg class="card-arrow" width="36" height="26" viewBox="0 0 36 26"><path d="M2 13h30M21 3l11 10-11 10" stroke="#6FCCEA" stroke-width="4" fill="none"/></svg>
</div>
<div class="card" style="left:893px;background:linear-gradient(170deg,#c0cbd3,#7d909e 55%,#3e4f5d)" role="img" aria-label="Person resting with an open book over the head">
  <div class="card-label">Licensed<b>The Clause</b></div>
  <svg class="card-arrow" width="36" height="26" viewBox="0 0 36 26"><path d="M2 13h30M21 3l11 10-11 10" stroke="#6FCCEA" stroke-width="4" fill="none"/></svg>
</div>
<a class="btn btn-outline">View All Services</a>

<!-- about -->
<div class="abs about-band"></div>
<h2 class="abs about-title serif">About Gray Harbor Plan</h2>
<p class="abs about-text">Gray Harbor Plan helps business owners stop groundless claims before they become lawsuits. Our licensed Clause requires the parties to a contract to notify each other, in writing, of any event that might impact it. A party that fails to comply loses ground on the "he said / she said" issues that decide most civil cases.<br>As Tom Wexley put it, an ounce of prevention is worth a pound of cure.</p>
<div class="abs about-frame"></div>
<div class="photo about-photo" role="img" aria-label="Lawyer in a suit meeting two clients across a desk"></div>
<a class="btn btn-learn">Learn More</a>

<!-- testimonials -->
<div class="abs reviews"></div>
<h2 class="abs reviews-title serif">What a Client's Say ?</h2>
<div class="abs reviews-rule"></div>
<svg class="abs" style="left:567px;top:2813px" width="66" height="66" viewBox="0 0 66 66"><circle cx="33" cy="33" r="30" stroke="#6FCCEA" stroke-width="3" fill="none"/><text x="33" y="44" text-anchor="middle" fill="#6FCCEA" font-family="Playfair Display,serif" font-size="30" font-weight="700">“</text></svg>
<svg class="abs" style="left:46px;top:2864px" width="42" height="42" viewBox="0 0 42 42"><circle cx="21" cy="21" r="19" stroke="#fff" stroke-width="3" fill="none"/><path d="M24 11 14 21l10 10" stroke="#fff" stroke-width="4" fill="none"/></svg>
<svg class="abs" style="left:1111px;top:2864px" width="42" height="42" viewBox="0 0 42 42"><circle cx="21" cy="21" r="19" stroke="#fff" stroke-width="3" fill="none"/><path d="m18 11 10 10-10 10" stroke="#fff" stroke-width="4" fill="none"/></svg>
<p class="abs quote">A former associate claimed I had promised him a share of a deal. Our contract used the Clause and he never notified us in writing, so the claim went nowhere. Worth far more than $9.95 a week.</p>
<svg class="abs" style="left:517px;top:3014px" width="166" height="24" viewBox="0 0 166 24"><circle cx="12" cy="12" r="10" fill="#fff"/><circle cx="60" cy="12" r="9" stroke="#6FCCEA" stroke-width="3" fill="none"/><circle cx="108" cy="12" r="10" fill="#fff"/><circle cx="154" cy="12" r="10" fill="#fff"/></svg>

<!-- consult + why -->
<div class="abs consult"></div>
<div class="abs why"></div>
<h2 class="abs block-title serif" style="left:45px;color:var(--white)">Free Consultant</h2>
<p class="abs block-text" style="left:45px;color:var(--mist)">Sued by an employee or business associate? Tell us about your case and we will review your position and your business structure free.</p>
<div class="field" style="left:45px;top:3272px;width:259px;height:64px">Your Name</div>
<div class="field" style="left:315px;top:3272px;width:259px;height:64px">Email</div>
<div class="field" style="left:45px;top:3347px;width:529px;height:64px">Subject</div>
<div class="field" style="left:45px;top:3423px;width:529px;height:129px">Your Message</div>
<a class="btn btn-send">Send message</a>

<h2 class="abs block-title serif" style="left:647px;color:var(--blue)">Why Choose US</h2>
<p class="abs block-text" style="left:645px;color:#333">Discounted fees, weekly attorney letters and the Clause are each worth far more than the $9.95 weekly membership.</p>
<div class="acc" style="top:3272px">
  <div class="acc-head">The Clause<svg width="32" height="22" viewBox="0 0 32 22"><path d="M3 19 16 5l13 14" stroke="#0094D4" stroke-width="5" fill="none"/></svg></div>
  <div class="acc-body">The Clause requires the parties to a contract to notify each other, in writing, of any fact or event that might impact it. A party that fails to comply gives you a significant advantage if the contract ends up in court, above all on issues with no concrete proof either way. Most claims stop before they start.</div>
</div>
<div class="acc" style="top:3499px">
  <div class="acc-head">Discounted Litigation<svg width="32" height="22" viewBox="0 0 32 22"><path d="M3 3l13 14L29 3" stroke="#0094D4" stroke-width="5" fill="none"/></svg></div>
</div>
<div class="acc" style="top:3574px">
  <div class="acc-head">Weekly Attorney Letters<svg width="32" height="22" viewBox="0 0 32 22"><path d="M3 3l13 14L29 3" stroke="#0094D4" stroke-width="5" fill="none"/></svg></div>
</div>

<!-- footer -->
<div class="abs footer"></div>
<h3 class="abs foot-title serif" style="left:48px">Getting in touch</h3>
<h3 class="abs foot-title serif" style="left:476px">Where to find us</h3>
<h3 class="abs foot-title serif" style="left:862px">Others</h3>
<div class="abs foot-line" style="left:46px;top:3818px">Call Us +1 555 010 3377</div>
<div class="abs foot-line" style="left:46px;top:3872px">Email help@ghp.example</div>
<a class="btn btn-contact">CONTACT US</a>
<div class="abs foot-line" style="left:475px;top:3822px">Harborview</div>
<div class="abs foot-line" style="left:475px;top:3876px;line-height:33px">Membership support<br>for business owners<br>$9.95 per week</div>
<div class="abs foot-line" style="left:861px;top:3822px">Privacy Policy</div>
<div class="abs foot-line" style="left:861px;top:3878px">FAQS</div>
<div class="abs foot-line" style="left:861px;top:3934px">Terms &nbsp;&amp; Conditions</div>
<div class="abs foot-rule"></div>
<div class="abs copyright">COPYRIGHT - 2022 ALL RIGHTS RESERVED</div>

</body>
</html>
```